Lowen Academy

I need different posters for a high school that displays positive messaging and the school's core values.
Want the design to look sleek for high school aged children

1. Poster #1
CORE VALUES:
• RESPECT
• RESPONSIBILITY
• LEADERSHIP
• PRIDE
• COMMUNITY

2. Acronym posters for the school
Empathy
Zeal
Respect
Aspire

3. additional acronym poster
Encourage
Zenith
Relationships
Accountability

```html
<!DOCTYPE html>
<html lang="en">
<head>
<meta charset="utf-8">
<title>Lowen Academy – Core Values &amp; Acronym Posters</title>
<link rel="stylesheet" href="https://fonts.googleapis.com/css2?family=Jost:wght@300;400;700&family=Poppins:wght@500;600&display=swap">
<style>
  :root {
    --page-bg: #d4d4d4;
    --navy: #0f2238;
    --navy-deep: #0b1a2c;
    --navy-soft: #183452;
    --gold: #e0962a;
    --gold-line: #d9922c;
    --cream: #f3e6c8;
    --white: #ffffff;
    --ring: rgba(255, 255, 255, 0.12);
    --rule: rgba(255, 255, 255, 0.22);
  }
  * { box-sizing: border-box; margin: 0; padding: 0; }
  html, body {
    width: 1200px; height: 2821px; overflow: hidden;
    background: var(--page-bg);
  }
  body { position: relative; font-family: "Poppins", sans-serif; }

  .poster {
    position: absolute;
    width: calc(var(--u) * 100);
    height: calc(var(--u) * 141.4);
    background: var(--navy);
    overflow: hidden;
    box-shadow: 0 10px 22px rgba(0, 0, 0, 0.35);
  }
  .poster--core { --u: 9px; left: 150px; top: 320px; }
  .poster--additional { --u: 5.2px; left: 60px; top: 1720px; }
  .poster--acronym { --u: 5.2px; left: 620px; top: 1720px; }

  .poster__photo {
    position: absolute; inset: 0;
    background:
      radial-gradient(ellipse at 50% 30%, rgba(40, 70, 95, 0.55), transparent 60%),
      linear-gradient(180deg, var(--navy-soft) 0%, var(--navy) 45%, var(--navy-deep) 100%);
  }
  .poster__frame { position: absolute; inset: 0; width: 100%; height: 100%; }
  .poster__frame path { fill: none; stroke: var(--gold-line); stroke-width: 1.2; vector-effect: non-scaling-stroke; }
  .poster__frame circle { fill: var(--cream); }

  .title-line {
    position: absolute; left: 0; right: 0; text-align: center;
    font-family: "Jost", sans-serif; line-height: 1;
  }
  .title-core { top: calc(var(--u) * 13.8); font-size: calc(var(--u) * 16.5); font-weight: 400; color: var(--gold); letter-spacing: -0.01em; }
  .title-values { top: calc(var(--u) * 27.6); font-size: calc(var(--u) * 17.5); font-weight: 700; color: var(--white); letter-spacing: -0.02em; }
  .title-kicker { top: calc(var(--u) * 11.5); font-size: calc(var(--u) * 5.2); font-weight: 400; color: var(--white); letter-spacing: 0.38em; padding-left: 0.38em; }
  .title-acronym { font-size: calc(var(--u) * 15); font-weight: 700; color: var(--gold); letter-spacing: -0.01em; }
  .poster--additional .title-acronym { top: calc(var(--u) * 17.5); }
  .poster--acronym .title-acronym { top: calc(var(--u) * 14.5); }

  /* core values list */
  .value-row {
    position: absolute;
    left: calc(var(--u) * 11.3); right: calc(var(--u) * 10.6);
    height: calc(var(--u) * 12.7);
    margin-top: calc(var(--u) * -6.35);
  }
  .value-row::after {
    content: ""; position: absolute;
    left: calc(var(--u) * 6.4); right: calc(var(--u) * 6.4);
    bottom: calc(var(--u) * 0.6);
    border-bottom: 1px solid var(--rule);
  }
  .value-row__icon {
    position: absolute; top: 0;
    width: calc(var(--u) * 12.7); height: calc(var(--u) * 12.7);
    border-radius: 50%; background: var(--ring);
    display: flex; align-items: center; justify-content: center;
  }
  .value-row__icon span {
    width: calc(var(--u) * 9); height: calc(var(--u) * 9);
    border-radius: 50%; background: var(--gold);
    display: flex; align-items: center; justify-content: center;
  }
  .value-row__icon svg { width: calc(var(--u) * 5); height: calc(var(--u) * 5); fill: var(--white); }
  .value-row--left .value-row__icon { left: 0; }
  .value-row--right .value-row__icon { right: 0; }
  .value-row__label {
    position: absolute; left: 0; right: 0; top: 50%; transform: translateY(-50%);
    text-align: center; color: var(--white);
    font-weight: 600; font-size: calc(var(--u) * 5); letter-spacing: 0.03em; line-height: 1;
  }

  /* acronym list */
  .letter-spine {
    position: absolute;
    left: calc(var(--u) * 15.5); width: calc(var(--u) * 17);
    top: calc(var(--u) * 39.8); height: calc(var(--u) * 71.4);
    border-radius: calc(var(--u) * 8.5);
    background: var(--ring);
  }
  .letter-spine::before {
    content: ""; position: absolute;
    left: calc(var(--u) * 1.4); right: calc(var(--u) * 1.4);
    top: calc(var(--u) * 1.4); bottom: calc(var(--u) * 1.4);
    border-radius: calc(var(--u) * 7.1);
    background: var(--gold);
  }
  .word-row {
    position: absolute;
    left: calc(var(--u) * 24); width: calc(var(--u) * 62.6);
    height: calc(var(--u) * 12.2); margin-top: calc(var(--u) * -6.1);
    border: 1px solid var(--rule); border-left: none;
    border-radius: 0 calc(var(--u) * 6.1) calc(var(--u) * 6.1) 0;
    background: rgba(255, 255, 255, 0.03);
  }
  .word-row__letter {
    position: absolute;
    left: calc(var(--u) * -5.7); top: 50%; margin-top: calc(var(--u) * -5.7);
    width: calc(var(--u) * 11.4); height: calc(var(--u) * 11.4);
    border-radius: 50%; background: var(--white);
    display: flex; align-items: center; justify-content: center;
    font-family: "Jost", sans-serif; font-weight: 700;
    font-size: calc(var(--u) * 8.4); color: var(--navy); line-height: 1;
    box-shadow: 0 calc(var(--u) * 0.4) calc(var(--u) * 0.8) rgba(0,0,0,0.25);
  }
  .word-row__word {
    position: absolute; top: 50%; transform: translateY(-50%);
    white-space: nowrap; line-height: 1;
    font-weight: 600; color: var(--white);
  }
  .poster--additional .word-row__word { left: calc(var(--u) * 12.5); font-size: calc(var(--u) * 5.8); }
  .poster--acronym .word-row__word { left: calc(var(--u) * 14); font-size: calc(var(--u) * 6.8); }
  .word-row__word b { color: var(--gold); font-weight: 600; }

  .row-1 { top: calc(var(--u) * 47); }
  .row-2 { top: calc(var(--u) * 61.3); }
  .row-3 { top: calc(var(--u) * 75.6); }
  .row-4 { top: calc(var(--u) * 89.9); }
  .row-5 { top: calc(var(--u) * 104.2); }

  .school-name {
    position: absolute; left: 0; right: 0; text-align: center;
    top: calc(var(--u) * 121.6);
    font-family: "Poppins", sans-serif; font-weight: 500;
    font-size: calc(var(--u) * 4); letter-spacing: 0.12em; color: var(--white); line-height: 1;
  }
</style>
</head>
<body>

<!-- Core values poster -->
<section class="poster poster--core" aria-label="Core values poster">
  <div class="poster__photo" role="img" aria-label="Faded photograph of students gathered outside the school, tinted navy"></div>
  <svg class="poster__frame" viewBox="0 0 100 141.4" preserveAspectRatio="none" aria-hidden="true">
    <path d="M28.8 53 H90.6 Q94.6 53 94.6 49 V9.7 Q94.6 5.7 90.6 5.7 H9.4 Q5.4 5.7 5.4 9.7 V131.7 Q5.4 135.7 9.4 135.7 H90.6 Q94.6 135.7 94.6 131.7 V114 Q94.6 110 90.6 110 H83"/>
    <circle cx="28.8" cy="53" r="0.7"/>
    <circle cx="83" cy="110" r="0.7"/>
  </svg>
  <h1 class="title-line title-core">CORE</h1>
  <h2 class="title-line title-values">VALUES</h2>

  <div class="value-row value-row--left" style="top: calc(var(--u) * 59);">
    <div class="value-row__icon"><span><svg viewBox="0 0 24 24"><path d="M12 21s-7.5-4.6-9.3-9.4C1.4 8.2 3.6 4.5 7.2 4.5c2 0 3.5 1.1 4.8 2.8 1.3-1.7 2.8-2.8 4.8-2.8 3.6 0 5.8 3.7 4.5 7.1C19.5 16.4 12 21 12 21z"/></svg></span></div>
    <p class="value-row__label">RESPECT</p>
  </div>
  <div class="value-row value-row--right" style="top: calc(var(--u) * 70.4);">
    <div class="value-row__icon"><span><svg viewBox="0 0 24 24"><circle cx="7" cy="7" r="2.4"/><circle cx="12" cy="6" r="2.6"/><circle cx="17" cy="7" r="2.4"/><path d="M3 13c0-2 1.8-3 4-3s4 1 4 3zM13 13c0-2 1.8-3 4-3s4 1 4 3z"/><path d="M2 16h5l3 2h5l6-3v2l-6 4H9l-3-2H2z"/></svg></span></div>
    <p class="value-row__label">RESPONSIBILITY</p>
  </div>
  <div class="value-row value-row--left" style="top: calc(var(--u) * 81.8);">
    <div class="value-row__icon"><span><svg viewBox="0 0 24 24"><path d="M12 2l1.4 2.9 3.1.4-2.3 2.1.6 3.1L12 9l-2.8 1.5.6-3.1-2.3-2.1 3.1-.4z"/><circle cx="5.5" cy="12" r="2.2"/><circle cx="18.5" cy="12" r="2.2"/><circle cx="12" cy="14" r="2.4"/><path d="M1.5 19c0-2 1.8-3.5 4-3.5s4 1.5 4 3.5zM14.5 19c0-2 1.8-3.5 4-3.5s4 1.5 4 3.5zM7.5 22c0-2.5 2-4.2 4.5-4.2s4.5 1.7 4.5 4.2z"/></svg></span></div>
    <p class="value-row__label">LEADERSHIP</p>
  </div>
  <div class="value-row value-row--right" style="top: calc(var(--u) * 93.2);">
    <div class="value-row__icon"><span><svg viewBox="0 0 24 24"><path d="M12 21s-7.5-4.6-9.3-9.4C1.4 8.2 3.6 4.5 7.2 4.5c2 0 3.5 1.1 4.8 2.8 1.3-1.7 2.8-2.8 4.8-2.8 3.6 0 5.8 3.7 4.5 7.1C19.5 16.4 12 21 12 21z"/><path d="M4 9.5h16M3.6 12.5h16.8M5.5 15.5h13" stroke="#e0962a" stroke-width="1.1"/></svg></span></div>
    <p class="value-row__label">PRIDE</p>
  </div>
  <div class="value-row value-row--left" style="top: calc(var(--u) * 104.6);">
    <div class="value-row__icon"><span><svg viewBox="0 0 24 24"><circle cx="12" cy="5" r="2.3"/><circle cx="6.5" cy="7.5" r="2.1"/><circle cx="17.5" cy="7.5" r="2.1"/><circle cx="4" cy="13" r="1.9"/><circle cx="20" cy="13" r="1.9"/><circle cx="12" cy="11" r="2.4"/><path d="M6.5 20c0-3.2 2.4-5.5 5.5-5.5s5.5 2.3 5.5 5.5zM1 18c0-2 1.3-3 3-3s3 1 3 3zM17 18c0-2 1.3-3 3-3s3 1 3 3z"/></svg></span></div>
    <p class="value-row__label">COMMUNITY</p>
  </div>

  <p class="school-name">LOWEN ACADEMY</p>
</section>

<!-- Additional acronym poster -->
<section class="poster poster--additional" aria-label="Additional acronym poster">
  <div class="poster__photo" role="img" aria-label="Faded photograph of the school campus, tinted navy"></div>
  <svg class="poster__frame" viewBox="0 0 100 141.4" preserveAspectRatio="none" aria-hidden="true">
    <path d="M87 47 H90.6 Q94.6 47 94.6 43 V9.7 Q94.6 5.7 90.6 5.7 H9.4 Q5.4 5.7 5.4 9.7 V131.7 Q5.4 135.7 9.4 135.7 H90.6 Q94.6 135.7 94.6 131.7 V108.2 Q94.6 104.2 90.6 104.2 H87"/>
    <path d="M87 61.3 H90.6 Q94.6 61.3 94.6 65.3 V71.6 Q94.6 75.6 90.6 75.6 H87"/>
  </svg>
  <p class="title-line title-kicker">ADDITIONAL</p>
  <h1 class="title-line title-acronym">ACRONYM</h1>

  <div class="letter-spine"></div>
  <div class="word-row row-1"><span class="word-row__letter">L</span><span class="word-row__word"><b>L</b>oyalty</span></div>
  <div class="word-row row-2"><span class="word-row__letter">O</span><span class="word-row__word"><b>O</b>wnership</span></div>
  <div class="word-row row-3"><span class="word-row__letter">W</span><span class="word-row__word"><b>W</b>ellbeing</span></div>
  <div class="word-row row-4"><span class="word-row__letter">E</span><span class="word-row__word"><b>E</b>ncourage</span></div>
  <div class="word-row row-5"><span class="word-row__letter">N</span><span class="word-row__word"><b>N</b>urture</span></div>

  <p class="school-name">LOWEN ACADEMY</p>
</section>

<!-- Acronym poster -->
<section class="poster poster--acronym" aria-label="Acronym poster">
  <div class="poster__photo" role="img" aria-label="Faded photograph of the school campus, tinted navy"></div>
  <svg class="poster__frame" viewBox="0 0 100 141.4" preserveAspectRatio="none" aria-hidden="true">
    <path d="M87 47 H90.6 Q94.6 47 94.6 43 V9.7 Q94.6 5.7 90.6 5.7 H9.4 Q5.4 5.7 5.4 9.7 V131.7 Q5.4 135.7 9.4 135.7 H90.6 Q94.6 135.7 94.6 131.7 V108.2 Q94.6 104.2 90.6 104.2 H87"/>
    <path d="M87 61.3 H90.6 Q94.6 61.3 94.6 65.3 V71.6 Q94.6 75.6 90.6 75.6 H87"/>
  </svg>
  <h1 class="title-line title-acronym">ACRONYM</h1>

  <div class="letter-spine"></div>
  <div class="word-row row-1"><span class="word-row__letter">L</span><span class="word-row__word"><b>L</b>isten</span></div>
  <div class="word-row row-2"><span class="word-row__letter">O</span><span class="word-row__word"><b>O</b>ptimism</span></div>
  <div class="word-row row-3"><span class="word-row__letter">W</span><span class="word-row__word"><b>W</b>isdom</span></div>
  <div class="word-row row-4"><span class="word-row__letter">E</span><span class="word-row__word"><b>E</b>mpathy</span></div>
  <div class="word-row row-5"><span class="word-row__letter">N</span><span class="word-row__word"><b>N</b>oble</span></div>

  <p class="school-name">LOWEN ACADEMY</p>
</section>

</body>
</html>
```